Pale Lantern Double Sided Flyer Design

We need a double sided flyer (1/3 of an A4 which is 99mm x 210mm) developed for our Newcastle(NSW) tour. This flyer will be placed in tourist information centres and hotels. We want it to direct people to our website or be able to make bookings over the phone.

About Us:-
We are a city walking tour company that runs tours day or night. We run both day and night and will incorporate real history / real Pale lantern. Some of the stories will be quite serious i.e.- there are infamous murders from 100 years ago, baffling court cases, even a bit of poetry written by murderers, suicides, love triangles, you name it. We will be telling the historical stories that tourists will not hear from any other tour provider. A bit of darkness, a bit of mystery and a bit of history theme.

We do no go for scares and let the very real stories deliver the entertainment for our guests. Our customers enjoy our tours, but it isn't light fun and frivolity. Our stories are being carefully crafted and are packed with unexpected twists, turns; revelations whilst remaining all 100% true. We deliver deep, rich, engaging stories.

Here are a few samples of quotes from the characters in our stories that may give you an idea of the kind of history we will cover:-

"There were bits of spines, bits of skulls, [and] finger bones spilled out all over the streets - I ended up filling three boxes. Children were playing with them for weeks”

"I had a close shave last night and now I want a close haircut.”

“She's a beautiful child', isn't she? She's the cause of all the trouble.”

“I did it because she would not come home with me.”

"I have killed my wife. I’m glad she’s dead.”

"Stand aside or I'll put a bullet through both of you."

“You villain, I'll teach you to take away my character."

“You’re not dead yet, you bastard!”

Our website, booking form and contact details can be viewed at www.palelantern.com.au

Target Market(s)

Tourists

Industry/Entity Type

Tour

Colors

Designer to choose colors to be used in the design.

Requirements
Must have
• Vertical orientation please.
• Please also include a reference to a discount offer of 25% using the promo code "WICK".
Nice to have
• FRONT FLYER INFORMATION
• - Pale Lantern Logo
• - "I have killed my wife; I'm glad she's dead."
• - Harbourside Hidden Lanes Walk
• - 25% Discount Offer Codeword WICK
• - web address at the base; www.palelantern.com.au
• BACK FLYER INFORMATION
• - "She's a beautiful child', isn't she? She's the cause of all the trouble.
• - Pale Lantern Logo at the base along with the web address www.palelantern.com.au
• - Blurb:- Pale lantern brings back Newcastle's hidden past, the forgotten past, the dark past that may not want to be remembered.
• Real stories from the streets around you. Discover the histories you won't hear anywhere else. The forgotten stories of yesteryear finally get a chance to be told. Through you they get to live again.
Should not have
• GENERAL
• Please do not include the phone number, email address or social media icons. We want to drive online bookings.

```html
<!DOCTYPE html>
<html lang="en">
<head>
<meta charset="utf-8">
<title>Pale Lantern – Double Sided Flyer</title>
<link rel="stylesheet" href="https://fonts.googleapis.com/css2?family=Montserrat:wght@500;600;700&family=Nunito+Sans:wght@400;600;700&family=Oswald:wght@400;500;600&display=swap">
<style>
  :root {
    --brand-red: #e42b2f;
    --ink: #111111;
    --paper: #ffffff;
    --stage: #e9e7e4;
    --body-text: #1c1c1c;
  }
  * { box-sizing: border-box; margin: 0; padding: 0; }
  html, body { width: 1200px; height: 1200px; overflow: hidden; }
  body { background: var(--stage); position: relative; font-family: "Montserrat", sans-serif; }

  .flyer {
    position: absolute; top: 122px; width: 451px; height: 958px;
    background: var(--paper); overflow: hidden;
    box-shadow: 0 6px 18px rgba(0,0,0,0.25);
  }
  .flyer--front { left: 127px; }
  .flyer--back { left: 622px; }
  .flyer__shapes { position: absolute; inset: 0; width: 451px; height: 958px; }

  .brand {
    position: absolute; left: 0; right: 0;
    display: flex; align-items: center; justify-content: center; gap: 8px;
    font-family: "Montserrat", sans-serif; font-weight: 600; font-size: 21px;
    color: var(--ink); letter-spacing: 0.5px;
  }
  .brand__dot { width: 14px; height: 14px; border-radius: 50%; background: var(--brand-red); }
  .flyer--front .brand { top: 102px; }
  .flyer--back .brand { top: 870px; }

  .web-address {
    position: absolute; left: 0; right: 0; bottom: 10px; text-align: center;
    font-family: "Nunito Sans", sans-serif; font-weight: 700; font-size: 13px;
    letter-spacing: 2.6px; color: var(--paper);
  }

  .discount-badge {
    position: absolute; left: 150px; top: 612px; width: 118px; height: 100px;
    color: var(--paper);
  }
  .discount-badge__figure { position: absolute; left: 13px; top: 18px; font-family: "Oswald", sans-serif; font-weight: 600; font-size: 38px; line-height: 1; }
  .discount-badge__percent { position: absolute; left: 56px; top: 17px; font-family: "Oswald", sans-serif; font-weight: 500; font-size: 17px; line-height: 1; }
  .discount-badge__label { position: absolute; left: 56px; top: 38px; font-family: "Oswald", sans-serif; font-weight: 500; font-size: 12px; line-height: 1; letter-spacing: 0; }
  .discount-badge__code { position: absolute; left: 8px; width: 100px; top: 74px; text-align: center; font-family: "Nunito Sans", sans-serif; font-size: 8.6px; white-space: nowrap; }

  .quote { position: absolute; left: 0; right: 0; text-align: center; font-weight: 600; color: var(--ink); }
  .quote em { font-style: normal; color: var(--brand-red); }
  .quote--front { top: 744px; font-size: 30px; line-height: 39px; }

  .tour-title { position: absolute; left: 0; right: 0; top: 838px; text-align: center; font-family: "Nunito Sans", sans-serif; }
  .tour-title__place { display: block; color: var(--brand-red); font-weight: 700; font-size: 23px; letter-spacing: 0.5px; line-height: 28px; }
  .tour-title__name { display: block; color: var(--ink); font-weight: 600; font-size: 19px; line-height: 26px; }

  .quote--back-lead { top: 537px; font-size: 23.5px; }
  .quote--back-main { top: 583px; font-size: 27px; line-height: 34px; }
  .quote--back-main em { text-transform: uppercase; }

  .blurb { position: absolute; left: 23px; right: 26px; top: 682px; font-family: "Nunito Sans", sans-serif; font-size: 12.6px; line-height: 16.5px; color: var(--body-text); }
  .blurb__label { position: absolute; left: 0; top: 4px; font-family: "Oswald", sans-serif; font-size: 18px; color: var(--brand-red); }
  .blurb__intro { margin-left: 58px; text-align: justify; }
  .blurb__body { margin-top: 16px; text-align: justify; }
</style>
</head>
<body>

<section class="flyer flyer--front">
  <svg class="flyer__shapes" viewBox="0 0 451 958">
    <defs>
      <linearGradient id="cityGrad" x1="0" y1="0" x2="1" y2="1">
        <stop offset="0" stop-color="#3a3c40"/>
        <stop offset="0.5" stop-color="#5b5e62"/>
        <stop offset="1" stop-color="#232527"/>
      </linearGradient>
    </defs>
    <rect role="img" aria-label="Aerial black and white photograph of city buildings and railway yards" x="0" y="70" width="451" height="640" fill="url(#cityGrad)"/>
    <path d="M0,0 H451 V90 C330,140 200,155 150,150 C90,142 30,118 0,95 Z" fill="var(--ink)"/>
    <path d="M0,0 H451 V86 C330,140 200,158 150,153 C90,146 30,124 0,104 Z" fill="var(--brand-red)"/>
    <path d="M0,0 H451 V84 C330,134 200,148 150,143 C90,136 30,112 0,86 Z" fill="var(--paper)"/>
    <path d="M0,560 C120,548 190,660 225,690 C260,660 330,548 451,560 L451,600 C330,600 270,690 225,712 C180,690 120,600 0,600 Z" fill="var(--ink)"/>
    <path d="M0,578 C120,566 190,676 225,700 C260,676 330,566 451,578 L451,634 C320,632 270,700 225,716 C180,700 130,632 0,634 Z" fill="var(--brand-red)"/>
    <path d="M0,634 C130,632 180,700 225,716 C270,700 320,632 451,634 L451,958 L0,958 Z" fill="var(--paper)"/>
    <path d="M146,620 L262,610 L268,717 L235,722 L272,738 L213,724 L152,729 Z" fill="var(--brand-red)"/>
    <path d="M154,628 L255,619 L260,709 L158,719 Z" fill="none" stroke="var(--paper)" stroke-width="1.4"/>
    <path d="M100,917 C250,902 380,905 451,932" fill="none" stroke="var(--ink)" stroke-width="4"/>
    <path d="M0,958 L0,944 C120,918 300,910 451,936 L451,958 Z" fill="var(--brand-red)"/>
  </svg>

  <div class="brand"><span class="brand__dot"></span>PALE LANTERN</div>

  <div class="discount-badge">
    <span class="discount-badge__figure">25</span>
    <span class="discount-badge__percent">%</span>
    <span class="discount-badge__label">DISCOUNT</span>
    <span class="discount-badge__code">Offer Codeword WICK</span>
  </div>

  <p class="quote quote--front">I have <em>killed</em> my wife<br>I'm glad she's <em>dead</em></p>

  <p class="tour-title">
    <span class="tour-title__place">HARBOURSIDE</span>
    <span class="tour-title__name">Hidden Lanes Walk</span>
  </p>

  <p class="web-address">www.palelantern.com.au</p>
</section>

<section class="flyer flyer--back">
  <svg class="flyer__shapes" viewBox="0 0 451 958">
    <defs>
      <linearGradient id="streetGrad" x1="0" y1="0" x2="0" y2="1">
        <stop offset="0" stop-color="#d6d6d6"/>
        <stop offset="0.45" stop-color="#8a8a8a"/>
        <stop offset="1" stop-color="#2e2e2e"/>
      </linearGradient>
      <linearGradient id="skylineGrad" x1="0" y1="0" x2="0" y2="1">
        <stop offset="0" stop-color="#6f8fb0"/>
        <stop offset="0.45" stop-color="#e7cf8e"/>
        <stop offset="0.55" stop-color="#6e7a63"/>
        <stop offset="1" stop-color="#4f6f92"/>
      </linearGradient>
    </defs>
    <rect role="img" aria-label="Vintage black and white photograph of a snowy old street with a lone walker" x="0" y="0" width="451" height="440" fill="url(#streetGrad)"/>
    <path d="M0,360 C80,350 140,380 180,430 L180,470 C140,430 80,418 0,420 Z" fill="var(--brand-red)"/>
    <path d="M451,360 C371,350 311,380 271,430 L271,470 C311,430 371,418 451,420 Z" fill="var(--brand-red)"/>
    <path d="M0,420 C80,418 140,440 170,480 C195,500 256,500 281,480 C311,440 371,418 451,420 L451,958 L0,958 Z" fill="var(--paper)"/>
    <circle cx="228" cy="398" r="102" fill="var(--brand-red)"/>
    <circle role="img" aria-label="Circular photograph of a city skyline reflected in a river at sunset" cx="228" cy="398" r="96" fill="url(#skylineGrad)"/>
    <path d="M100,917 C250,902 380,905 451,932" fill="none" stroke="var(--ink)" stroke-width="4"/>
    <path d="M0,958 L0,944 C120,918 300,910 451,936 L451,958 Z" fill="var(--brand-red)"/>
  </svg>

  <p class="quote quote--back-lead">She's a <em>beautiful child</em>, isn't she?</p>
  <p class="quote quote--back-main">She's the cause of<br><em>all the trouble</em></p>

  <div class="blurb">
    <span class="blurb__label">Blurb :</span>
    <p class="blurb__intro">Pale lantern brings back Newcastle's hidden past, the forgotten past, the dark past that may not want to be remembered.</p>
    <p class="blurb__body">Real stories from the streets around you. Discover the histories you won't hear anywhere else. The forgotten stories of yesteryear finally get a chance to be told. Through you they get to live again</p>
  </div>

  <div class="brand"><span class="brand__dot"></span>PALE LANTERN</div>

  <p class="web-address">www.palelantern.com.au</p>
</section>

</body>
</html>
```